TOTR 'Lower Third' for documentary TV series

Create a lower third for the series Drifters of the Ridge (airs 2019) - we are in nature for the entire series, they use birch bark canoes to travel, they eat what they can find/catch including fish and beaver, no modern technology, must be able to have name and below where they are from. thanks

Target Market(s)

TV Series

Industry/Entity Type

Tv

Colors

Designer to choose colors to be used in the design.

Requirements
Must have
• pops from screen, keep in mind we have lots of lakes, sky and forest
Nice to have
• stands out
Should not have
• i'm open

```html
<!DOCTYPE html>
<html lang="en">
<head>
<meta charset="utf-8">
<title>TOTR Lower Third</title>
<link rel="stylesheet" href="https://fonts.googleapis.com/css2?family=Signika:wght@600;700&display=swap">
<style>
  :root {
    --band-yellow: #e0c23c;
    --band-yellow-dark: #cfae2a;
    --ink: #1b1914;
    --scene-water: #3d5a6e;
    --scene-rock: #4a4640;
    --scene-grass: #7c7a3a;
    --scene-canoe: #b0623a;
  }
  * { box-sizing: border-box; margin: 0; padding: 0; }
  html, body {
    width: 1200px;
    height: 900px;
    overflow: hidden;
    background: #111;
  }
  .frame {
    position: relative;
    width: 1200px;
    height: 900px;
    overflow: hidden;
    font-family: "Signika", sans-serif;
  }
  .footage {
    position: absolute;
    inset: 0;
    background:
      radial-gradient(ellipse 40% 35% at 78% 55%, var(--scene-canoe) 0%, transparent 70%),
      linear-gradient(160deg, var(--scene-rock) 0%, var(--scene-rock) 30%, var(--scene-water) 55%, var(--scene-grass) 80%, #3a3a2a 100%);
  }
  .band {
    position: absolute;
    background: linear-gradient(180deg, var(--band-yellow) 0%, var(--band-yellow) 80%, var(--band-yellow-dark) 100%);
    color: var(--ink);
    display: flex;
    align-items: center;
  }
  .band-name {
    left: 64px;
    top: 654px;
    width: 1068px;
    height: 124px;
    clip-path: polygon(1% 2%, 20% 0, 55% 3%, 99% 0, 100% 40%, 98.5% 100%, 60% 97%, 25% 100%, 0 98%, 1.5% 50%);
  }
  .band-origin {
    left: 140px;
    top: 802px;
    width: 908px;
    height: 78px;
    clip-path: polygon(0 4%, 40% 0, 100% 3%, 99% 55%, 100% 100%, 50% 96%, 0 100%, 1% 50%);
    justify-content: center;
  }
  .series-mark {
    position: absolute;
    left: 28px;
    top: 50%;
    transform: translateY(-50%);
    width: 240px;
    font-weight: 700;
    font-size: 26px;
    line-height: 1.05;
    text-transform: uppercase;
    letter-spacing: 0.5px;
    color: var(--ink);
  }
  .person-name {
    position: absolute;
    left: 270px;
    right: 100px;
    text-align: center;
    font-weight: 700;
    font-size: 90px;
    letter-spacing: 1px;
    text-transform: uppercase;
    line-height: 1;
  }
  .person-origin {
    font-weight: 600;
    font-size: 48px;
    line-height: 1;
  }
</style>
</head>
<body>
  <div class="frame">
    <div class="footage" role="img" aria-label="Documentary footage: two travellers resting on a rocky lakeshore beside a birch bark canoe and tall reeds"></div>

    <div class="band band-name">
      <div class="series-mark">Drifters of<br>the Ridge</div>
      <h1 class="person-name">Dale Merritt</h1>
    </div>

    <div class="band band-origin">
      <p class="person-origin">Kenora, ON</p>
    </div>
  </div>
</body>
</html>
```